Kavenzira Wines

A Red Wine Label for future Wine Concept called Kavenzira Wine. The back label will have the following words which capture the essence of the wine "I am sworn to the secrecy about the origins of this wine but I can assure you it’s from the best cellars of Africa. Kavenzira is an African (Shona) name which loosely means honour, praise or to be held in high exteem. Hold on to your hats because this wine is a whirlwind of flavours. It's dark, spicy and fruity flavours will attack the palate with warm aggression and intent whilst being served with Sadza/ Nsima and roasted beef accompanied with mufushwa (dried vegetables) cooked in grounded nut paste. The inspiring flame, style and mood of an African braai, together with its outlandish flavours popping in and out of the glass, Kavenzira will make every serving a gesture of respect and distinction!!!"
Updates

I will be buying wine packed in unbranded bottles then Brand it as Kavenzira on my own Kavenzira label for some African event theme. The wines will be South African a Shiraz. So I need a back label with message placed in brief and front label for a red wine bottle. I have attached some old labels for the wine so I need a redesign of the l label for have a morden and African feel to it                                   

Please

Target Market(s)

Appeal to general populace and those with an afrocentric feel

Requirements
Must have
• Back and front labels, simplicity
Should not have
• Too many colours

```html
<!DOCTYPE html>
<html lang="en">
<head>
<meta charset="utf-8">
<title>Kavenzira Wines – Shiraz Labels</title>
<link rel="stylesheet" href="https://fonts.googleapis.com/css2?family=Delius&family=Macondo&display=swap">
<style>
  :root {
    --page: #ffffff;
    --wine: #931e1a;
    --bevel-light: #c98a88;
    --bevel-mid: #a8403c;
    --bevel-dark: #6a0d0b;
    --cream: #f8f3e4;
    --cream-edge: #efe4c9;
    --tree-red: #b8201f;
    --tree-green: #1f6b2c;
    --text: #ffffff;
    --ink: #000000;
  }
  * { box-sizing: border-box; margin: 0; padding: 0; }
  html, body {
    width: 1200px;
    height: 566px;
    overflow: hidden;
    background: var(--page);
  }
  .canvas {
    position: relative;
    width: 1200px;
    height: 566px;
  }
  .label {
    position: absolute;
    top: 33px;
    width: 509px;
    height: 509px;
    background: var(--wine);
    border-style: solid;
    border-width: 14px;
    border-color: var(--bevel-light) var(--bevel-dark) var(--bevel-dark) var(--bevel-mid);
    font-family: "Delius", sans-serif;
    color: var(--text);
    text-align: center;
  }
  .label--front { left: 33px; }
  .label--back { left: 655px; }

  .emblem-frame {
    position: absolute;
    left: 99px;
    top: 31px;
    width: 282px;
    height: 282px;
    background: var(--wine);
    border-style: solid;
    border-width: 10px;
    border-color: var(--bevel-light) var(--bevel-dark) var(--bevel-dark) var(--bevel-mid);
  }
  .emblem-card {
    position: absolute;
    left: 26px;
    top: 23px;
    width: 210px;
    height: 226px;
    background: radial-gradient(circle at 50% 45%, var(--cream) 60%, var(--cream-edge) 100%);
  }
  .emblem-tree {
    position: absolute;
    left: 17px;
    top: 8px;
    width: 176px;
    height: 212px;
    border-radius: 50% 50% 10% 10% / 45% 45% 6% 6%;
    background: radial-gradient(ellipse at 50% 55%, var(--tree-green) 0%, var(--tree-green) 30%, var(--tree-red) 70%);
  }

  .wine-name {
    font-family: "Macondo", cursive;
    font-weight: 400;
    line-height: 1;
    text-shadow: -1.5px -1.5px 0 var(--ink), 1.5px -1.5px 0 var(--ink), -1.5px 1.5px 0 var(--ink), 1.5px 1.5px 0 var(--ink);
  }
  .wine-detail {
    line-height: 1;
  }
  .front-text {
    position: absolute;
    left: 0;
    right: 0;
    top: 340px;
  }
  .front-text .wine-name { font-size: 46px; margin-bottom: 4px; }
  .front-text .wine-detail { font-size: 27px; margin-top: 6px; }

  .back-tree {
    position: absolute;
    left: 90px;
    top: 200px;
    width: 300px;
    height: 295px;
    border-radius: 50% 50% 10% 10% / 45% 45% 4% 4%;
    background: radial-gradient(ellipse at 50% 50%, rgba(31,107,44,0.45) 0%, rgba(184,32,31,0.35) 55%, rgba(147,30,26,0) 75%);
  }
  .story {
    position: absolute;
    left: 14px;
    right: 14px;
    top: 66px;
    font-size: 16.5px;
    line-height: 21.4px;
  }
  .back-text {
    position: absolute;
    left: 0;
    right: 0;
    top: 368px;
  }
  .back-text .wine-name { font-size: 46px; margin-bottom: 2px; }
  .back-text .wine-detail { font-size: 27px; margin-top: 6px; }
</style>
</head>
<body>
<main class="canvas">
  <section class="label label--front" aria-label="Front label">
    <div class="emblem-frame">
      <div class="emblem-card">
        <div class="emblem-tree" role="img" aria-label="Illustrated tree with red leaves and a green-to-red trunk"></div>
      </div>
    </div>
    <div class="front-text">
      <h1 class="wine-name">Kavenzira</h1>
      <p class="wine-detail">Shiraz</p>
      <p class="wine-detail">South Africa</p>
      <p class="wine-detail">2013</p>
    </div>
  </section>

  <section class="label label--back" aria-label="Back label">
    <div class="back-tree" role="img" aria-label="Faint illustrated tree in red and green behind the text"></div>
    <p class="story">I am sworn to the secrecy about the origins of this wine but I can assure you it’s from the best cellars of Africa. Kavenzira is an African (Shona) name which loosely means honour, praise or to be held in high exteem. Hold on to your hats because this wine is a whirlwind of flavours. It’s dark, spicy and fruity flavours will attack the palate with warm aggression and intent whilst being served with Sadza/ Nsima and roasted beef accompanied with mufushwa (dried vegetables) cooked in grounded nut paste. The inspiring flame, style and mood of an African braai, together with its outlandish flavours popping in and out of the glass, Kavenzira will make every serving a gesture of respect and distinction!</p>
    <div class="back-text">
      <h2 class="wine-name">Kavenzira</h2>
      <p class="wine-detail">Shiraz</p>
      <p class="wine-detail">South Africa</p>
    </div>
  </section>
</main>
</body>
</html>
```